Modernise Business Card

Our company has been operating for 10 years. With the start of the new decade we are looking to refresh our business card design. We manufacture a range of industrial product shipping to customers internationally. A copy of our current card, both sides, is attached. We are looking for a mature professional appearance.

```html
<!DOCTYPE html>
<html lang="en">
<head>
<meta charset="utf-8">
<title>Korvex Business Card</title>
<link href="https://fonts.googleapis.com/css2?family=Poppins:wght@400;500;600;700&display=swap" rel="stylesheet">
<style>
  :root {
    --stage: #2b2b2d;
    --paper: #ffffff;
    --ink: #2f2f33;
    --brand-blue: #20a8d4;
    --brand-grey: #6e6e72;
    --rule: #9a9a9e;
  }
  * { box-sizing: border-box; margin: 0; padding: 0; }
  html, body { width: 1200px; height: 675px; overflow: hidden; }
  body {
    background: var(--stage);
    font-family: "Poppins", sans-serif;
    color: var(--ink);
    position: relative;
  }
  .card {
    position: absolute;
    top: 180px;
    width: 520px;
    height: 300px;
    background: var(--paper);
    border-radius: 10px;
    overflow: hidden;
    box-shadow: 0 10px 30px rgba(0,0,0,0.35);
  }
  .card--front { left: 50px; }
  .card--back { left: 630px; }

  /* Front */
  .card--front .edge-stripe {
    position: absolute; left: 0; right: 0; bottom: 0;
    height: 8px; background: var(--brand-blue);
  }
  .wordmark {
    font-weight: 700;
    color: var(--brand-blue);
    letter-spacing: -1px;
    line-height: 1;
    display: flex;
    align-items: center;
    gap: 10px;
  }
  .wordmark__dot {
    width: 14px; height: 14px; background: var(--brand-grey);
  }
  .card--front .wordmark {
    font-size: 58px;
    justify-content: center;
    margin-top: 34px;
  }
  .person-name {
    text-align: center;
    font-weight: 600;
    font-size: 19px;
    letter-spacing: 0.5px;
    margin-top: 16px;
  }
  .person-name .surname { color: var(--brand-blue); }
  .tagline {
    text-align: center;
    font-size: 11.5px;
    margin-top: 2px;
  }
  .details {
    display: flex;
    justify-content: center;
    margin-top: 18px;
    font-size: 11px;
    line-height: 1.45;
  }
  .contact-list {
    list-style: none;
    text-align: right;
    padding-right: 16px;
    border-right: 1px solid var(--rule);
  }
  .contact-list li { display: flex; justify-content: flex-end; align-items: center; gap: 6px; }
  .contact-list .label { color: var(--brand-blue); }
  .contact-list svg { width: 11px; height: 11px; flex: none; }
  .contact-list .no-icon { padding-right: 17px; }
  .address {
    font-style: normal;
    padding-left: 16px;
    padding-top: 26px;
  }

  /* Back */
  .card--back .wordmark {
    position: absolute; left: 34px; top: 34px;
    font-size: 50px;
  }
  .card--back .tagline {
    position: absolute; left: 36px; top: 98px;
    text-align: left;
    font-size: 11px;
    font-weight: 600;
    text-transform: uppercase;
    line-height: 1.5;
    max-width: 260px;
  }
  .back-shapes { position: absolute; inset: 0; width: 100%; height: 100%; }
</style>
</head>
<body>

<section class="card card--front" aria-label="Business card front">
  <div class="wordmark"><span class="wordmark__dot"></span>Korvex</div>
  <p class="person-name">ALAN <span class="surname">PIERCE</span></p>
  <p class="tagline">Hydraulic Adapters hose Fittings Quick Couplings</p>
  <div class="details">
    <ul class="contact-list">
      <li class="no-icon"><span><span class="label">China:</span> +86 100 5550 0142</span></li>
      <li><span><span class="label">Australia:</span> +61 400 555 017</span>
        <svg viewBox="0 0 12 12" aria-hidden="true"><rect x="3" y="0.5" width="6" height="11" rx="1.2" fill="none" stroke="#20a8d4" stroke-width="1.2"/><circle cx="6" cy="9.5" r="0.7" fill="#20a8d4"/></svg></li>
      <li><span><span class="label">Email:</span> apierce@korvexfittings.com</span>
        <svg viewBox="0 0 12 12" aria-hidden="true"><rect x="0.5" y="2" width="11" height="8" fill="#20a8d4"/><path d="M0.5 2 L6 6.5 L11.5 2" fill="none" stroke="#fff" stroke-width="1"/></svg></li>
      <li><span><span class="label">Web:</span> www.korvexfittings.com</span>
        <svg viewBox="0 0 12 12" aria-hidden="true"><circle cx="6" cy="6" r="5.3" fill="none" stroke="#20a8d4" stroke-width="1.2"/><ellipse cx="6" cy="6" rx="2.2" ry="5.3" fill="none" stroke="#20a8d4" stroke-width="1"/><line x1="0.7" y1="6" x2="11.3" y2="6" stroke="#20a8d4" stroke-width="1"/></svg></li>
    </ul>
    <address class="address">
      1208-4, Lianhe Tower<br>
      71 Harbour Road, Central District<br>
      Ningbo 315000 China
    </address>
  </div>
  <div class="edge-stripe"></div>
</section>

<section class="card card--back" aria-label="Business card back">
  <svg class="back-shapes" viewBox="0 0 520 300" preserveAspectRatio="none" aria-hidden="true">
    <path d="M430 300 L430 200 Q430 150 480 150 L520 150 L520 300 Z" fill="#6e6e72"/>
    <path d="M250 300 L300 190 L430 170 L385 300 Z" fill="#20a8d4"/>
  </svg>
  <div class="wordmark"><span class="wordmark__dot"></span>Korvex</div>
  <p class="tagline">Hydraulic Adapters hose Fittings<br>Quick Couplings</p>
</section>

</body>
</html>
```